Brantmoor Financial Coaching LLC - Needed clean black business card

Business card for personal financial coaching practice located on Las Vegas NV, new startup. Back of card needs to have "how it works" to match the website.

Font styles to use
Sans Serif

Colors

Designer to choose colors to be used in the design.

```html
<!DOCTYPE html>
<html lang="en">
<head>
<meta charset="utf-8">
<title>Brantmoor Financial Coaching – Business Card</title>
<link href="https://fonts.googleapis.com/css2?family=Figtree:wght@400;700;800&display=swap" rel="stylesheet">
<style>
  :root {
    --backdrop: #5e4a35;
    --card: #000000;
    --ink: #d9d9d9;
    --ink-soft: #e6e6e6;
    --rule: #cfcfcf;
  }
  * { margin: 0; padding: 0; box-sizing: border-box; }
  html, body {
    width: 900px;
    height: 1200px;
    overflow: hidden;
    background: var(--backdrop);
    font-family: "Figtree", "Helvetica Neue", Arial, sans-serif;
  }
  .canvas { position: relative; width: 900px; height: 1200px; }

  .card {
    position: absolute;
    left: 75px;
    width: 768px;
    height: 438px;
    background: var(--card);
    color: var(--ink);
  }
  .card--front { top: 133px; }
  .card--back { top: 629px; }

  .rule {
    position: absolute;
    width: 3px;
    background: var(--rule);
  }

  /* Front */
  .front__rule-top { left: 47px; top: 42px; height: 62px; }
  .front__rule-side { left: 719px; top: 174px; height: 222px; }
  .company {
    position: absolute;
    right: 46px;
    top: 47px;
    text-align: right;
    font-weight: 700;
    font-size: 22px;
    line-height: 25px;
    letter-spacing: 2.2px;
    text-transform: uppercase;
  }
  .person {
    position: absolute;
    left: 44px;
    top: 188px;
    font-weight: 800;
    font-size: 28px;
    line-height: 31px;
    letter-spacing: 2px;
    text-transform: uppercase;
  }
  .contact {
    position: absolute;
    left: 47px;
    top: 315px;
    list-style: none;
    font-weight: 400;
    font-size: 19px;
    line-height: 27.5px;
    letter-spacing: 1.6px;
    text-transform: uppercase;
  }

  /* Back */
  .back__rule-side { left: 714px; top: 48px; height: 345px; }
  .how-title {
    position: absolute;
    left: 56px;
    top: 64px;
    font-weight: 800;
    font-size: 28px;
    letter-spacing: 1.6px;
  }
  .how-text {
    position: absolute;
    left: 54px;
    top: 164px;
    font-size: 18.5px;
    line-height: 27.5px;
    color: var(--ink-soft);
  }
  .how-url {
    display: block;
    margin-top: 2px;
    font-weight: 700;
    font-size: 23px;
    letter-spacing: 3.6px;
  }
  .location {
    position: absolute;
    left: 54px;
    top: 364px;
    display: flex;
    align-items: center;
    gap: 10px;
    font-size: 19px;
    letter-spacing: 1.6px;
    text-transform: uppercase;
  }
  .location svg { width: 21px; height: 28px; fill: var(--ink); }
</style>
</head>
<body>
<main class="canvas">

  <section class="card card--front" aria-label="Card front">
    <span class="rule front__rule-top"></span>
    <p class="company">Brantmoor<br>Financial Coaching LLC</p>
    <h1 class="person">Dana<br>Brantmoor</h1>
    <ul class="contact">
      <li>702-555-0148</li>
      <li>dana@brantmoorfinancialcoaching.com</li>
      <li>www.brantmoorfinancialcoaching.com</li>
    </ul>
    <span class="rule front__rule-side"></span>
  </section>

  <section class="card card--back" aria-label="Card back">
    <h2 class="how-title">How It Works</h2>
    <p class="how-text">
      All free one-time consultations are in-person meetings only.<br>
      Paid appointments may be scheduled for in-person or virtual<br>
      meetings. Select the session, date and time that works best for<br>
      your schedule. Start your journey of financial freedom at
      <span class="how-url">brantmoorfinancialcoaching.com</span>
    </p>
    <p class="location">
      <svg viewBox="0 0 24 32" aria-hidden="true">
        <path d="M12 0C5.4 0 0 5.3 0 11.9 0 20.6 12 32 12 32s12-11.4 12-20.1C24 5.3 18.6 0 12 0zm0 16.5a4.6 4.6 0 1 1 0-9.2 4.6 4.6 0 0 1 0 9.2z"/>
      </svg>
      4120 W Sable Ridge Rd #105-C, Las Vegas, NV 89147
    </p>
    <span class="rule back__rule-side"></span>
  </section>

</main>
</body>
</html>
```